We need a new letterhead design for a 20 year old consulting company. Ideally jpg (or other) image that can be dropped onto a word/publisher document. Currently we have a 'design' header and 'detail' footer (with address etc), and this works well, but is not essential. The letterhead/footer must be suitable for portrait and landscape (or 2 separate images to cater for both alignments) and must be suitable for in-office printing (ie doesn't lose content outside of printer margins)

Our business card includes a cutout jigsaw piece, so it is essential that a jigsaw image is included in the design. Our most recent design also included clouds, but I'm over this. Use SUBDUED greyish/blue colouring.

I've attached the old letterhead (file names letterhead fat and letterhead master), and one I've mocked up (TVRB letterhead Nov 12) and market tested (new name is TVRB Strategy), so this should provide a starting point. NOTE COMPANY NAME IS TVRB Strategy - quite a few designs have come in with our old company name.

The design needs to communicate simplicity, experience, ideas. our tagline is "clarity and direction", but we also use "when you need ideas". Don't include these in the design, we change them quite often.

Many thanks

Delphine

Hi Designers

thanks for the first suite of designs. Having seen them, I need to be a little more specific about some things:

We are no longer using "Lateral Planners", the logo is TVRB Strategy (preferably with the word 'strategy' underneath TVRB and the same size

I don't like watermarks (sorry), so I'm ignoring those, and if I like a design it will have all watermarks removed.

I like the 'swoop' that we have been using - I'm not stuck on it, but like the designs with a bit more creativity better

I don't like boxes of text (could do that myself on a word processor), it needs to look like it's been designed by a graphic designer

Please keep the colours blue/grey (as per my TVRB Strategy attachment)

Cheers

Delphine

Hello again

I use the letterhead for report covers, so the image at the header and footer need to frame the page - designs that just use text at the top or bottom won't work because they won't 'stand out' when used as a cover.

Thanks

K

Hi designers, some lovely work coming through. Pls don't forget that I'm after a letterhead that I'll be printing on ink and laser printers, So anything close to the edge of the paper (eg address) won't print. It will be necessary for the design to work within printable range.

Ta

K

Reason: Hi everyone Because of the Christmas Holidays, I have decided to extend the deadline by 2 weeks. Cheers Delphine

Target Market(s)

corporate and government clients, CEOs etc

Industry/Entity Type

Landscape

Requirements
Must have
• Blue/grey colours
Jigsaw logo
Suitable for portrait and landscape
name: TVRB Strategy
Nice to have
• Fresh and contemporary
Should not have
• the old company name (TVRB Lateral Planners)
important content (design/contact details) that will not print on ink/laser printer

```html
<!DOCTYPE html>
<html lang="en">
<head>
<meta charset="utf-8">
<title>TVRB Strategy Letterhead</title>
<link rel="stylesheet" href="https://fonts.googleapis.com/css2?family=Arimo:wght@400;700&family=Great+Vibes&display=swap">
<style>
  :root {
    --backdrop: #e4e5e7;
    --paper: #ffffff;
    --navy: #1d4f86;
    --navy-deep: #163f6e;
    --sky: #2a8fc4;
    --body-text: #4a4a4a;
    --swoop-dark: #6d6e70;
    --swoop-light: #d6d7d9;
    --square: #b9c6e4;
  }
  * { margin: 0; padding: 0; box-sizing: border-box; }
  html, body {
    width: 1200px; height: 750px; overflow: hidden;
    background: var(--backdrop);
    font-family: "Arimo", Arial, sans-serif;
  }
  .stage { position: relative; width: 1200px; height: 750px; }
  .sheet {
    position: absolute; top: 84px;
    width: 422px; height: 599px;
    background: var(--paper);
    overflow: hidden;
  }
  .sheet--letter { left: 162px; }
  .sheet--blank { left: 622px; }

  .brand { position: absolute; left: 22px; top: 16px; display: flex; align-items: flex-start; gap: 12px; }
  .brand__name {
    font-weight: 700; color: var(--navy);
    display: flex; flex-direction: column; line-height: 1;
  }
  .brand__word--main { font-size: 34px; letter-spacing: 1px; }
  .brand__word--sub { font-size: 15px; letter-spacing: 2.4px; margin-top: 6px; }
  .brand__square { width: 30px; height: 30px; background: var(--square); margin-top: 2px; }

  .contact {
    position: absolute; left: 238px; top: 26px;
    color: var(--navy); font-size: 8.2px; line-height: 11px; font-style: normal;
  }
  .contact__address { font-size: 10.5px; line-height: 13px; }
  .contact__line { display: flex; align-items: center; gap: 3px; }
  .contact__icon { width: 8px; height: 8px; fill: var(--navy); }

  .letter {
    position: absolute; left: 25px; top: 140px; width: 386px;
    color: var(--body-text); font-size: 8.4px; line-height: 14.2px;
  }
  .letter__greeting { font-weight: 700; color: #333; margin-bottom: 13px; }
  .letter p { margin-bottom: 14px; }
  .letter__closing { margin-top: 12px; }
  .letter__signature {
    font-family: "Great Vibes", cursive; font-size: 17px; color: #444;
    margin-top: 10px; margin-left: 2px;
  }

  .footer { position: absolute; left: 0; bottom: 0; width: 422px; height: 100px; }
  .footer__swoop { position: absolute; inset: 0; }
  .footer__brand {
    position: absolute; left: 276px; top: 54px;
    display: flex; align-items: center; gap: 8px;
  }
  .footer__name {
    font-weight: 700; font-size: 26px; line-height: 1;
    color: var(--navy); letter-spacing: 1px;
  }
  .footer__square { width: 30px; height: 30px; background: var(--square); }
</style>
</head>
<body>
<main class="stage">

  <section class="sheet sheet--letter">
    <header>
      <div class="brand">
        <div class="brand__name">
          <span class="brand__word--main">TVRB</span>
          <span class="brand__word--sub">strategy</span>
        </div>
        <span class="brand__square"></span>
      </div>
      <address class="contact">
        <div class="contact__address">14 Larkin Lane Glenwood SA 5172</div>
        <div class="contact__line">
          <svg class="contact__icon" viewBox="0 0 10 10"><path d="M2 1h2l1 2.5-1.3.8a5 5 0 0 0 2 2l.8-1.3L9 6v2a1 1 0 0 1-1 1A8 8 0 0 1 1 2a1 1 0 0 1 1-1z"/></svg>
          (+618) 8123 4567 |
          <svg class="contact__icon" viewBox="0 0 10 10"><path d="M1 2h8v6H1z M1 2l4 3 4-3" fill="none" stroke="#1d4f86" stroke-width="1"/></svg>
          info@tvrb.com.au
        </div>
        <div>www.tvrb.com.au</div>
      </address>
    </header>

    <article class="letter">
      <div class="letter__greeting">Dear Customer,</div>
      <p>Lorem ipsum dolor sit amet, consectetur adipiscing elit. Donec elementum velit sit amet libero fringilla adipiscing. Aliquam sollicitudin, leo vitae molestie facilisis, tellus ligula varius velit, vitae tincidunt lacus purus vitae nulla. Nulla imperdiet, odio quis ultrices ornare, diam est dictum lacus, et vehicula est magna at metus. Integer mattis lorem quis tortor accumsan ultrices ac ut massa. Duis eget metus ut risus scelerisque ornare quis eget dui. Aliquam lobortis dolor vitae magna volutpat eu facilisis tellus molestie. Sed a purus quis nibh lacinia interdum ut at leo.</p>
      <p>Integer consequat velit quis elit hendrerit imperdiet. Donec felis velit, volutpat vel convallis nec, sollicitudin et nulla. Pellentesque sodales elementum aliquam. Donec convallis, turpis sit amet laoreet ultricies, enim est elementum magna, dictum lobortis eros tellus quis diam. Nunc suscipit augue non nisl volutpat volutpat. Ut egestas ultrices purus, eget varius nibh placerat in. Cras leo ante, congue id ultricies a, ornare eu est. Curabitur eleifend tincidunt mi eget tristique.</p>
      <p>Etiam arcu augue, ornare vitae consectetur luctus, tincidunt vitae urna. Lorem ipsum dolor sit amet, consectetur adipiscing elit. Donec vitae tortor quis orci adipiscing lobortis. Morbi aliquet orci quis mi viverra sollicitudin. Sed eget pellentesque turpis. Aliquam commodo sodales ultrices. Nullam ut elit vitae elit suscipit porttitor viverra non mi. Donec diam mi, tincidunt nec sodales vestibulum, iaculis a urna. Nulla facilisi. Integer consequat velit quis elit hendrerit imperdiet.</p>
      <div class="letter__closing">Your Sincerelly</div>
      <div class="letter__signature">Signature</div>
    </article>

    <footer class="footer">
      <svg class="footer__swoop" viewBox="0 0 422 100" preserveAspectRatio="none">
        <defs>
          <linearGradient id="swoopGreyA" x1="0" x2="1">
            <stop offset="0" stop-color="#6d6e70"/>
            <stop offset="1" stop-color="#d6d7d9"/>
          </linearGradient>
          <linearGradient id="bandBlueA" x1="0" x2="1">
            <stop offset="0" stop-color="#2a8fc4"/>
            <stop offset="1" stop-color="#163f6e"/>
          </linearGradient>
        </defs>
        <path d="M0 58 C120 66 240 76 330 85 C230 81 110 73 0 66 Z" fill="url(#swoopGreyA)"/>
        <path d="M0 71 C130 86 300 92 422 70 V100 H0 Z" fill="url(#bandBlueA)"/>
      </svg>
      <div class="footer__brand">
        <span class="footer__name">TVRB</span>
        <span class="footer__square"></span>
      </div>
    </footer>
  </section>

  <section class="sheet sheet--blank">
    <header>
      <div class="brand">
        <div class="brand__name">
          <span class="brand__word--main">TVRB</span>
          <span class="brand__word--sub">strategy</span>
        </div>
        <span class="brand__square"></span>
      </div>
      <address class="contact">
        <div class="contact__address">14 Larkin Lane Glenwood SA 5172</div>
        <div class="contact__line">
          <svg class="contact__icon" viewBox="0 0 10 10"><path d="M2 1h2l1 2.5-1.3.8a5 5 0 0 0 2 2l.8-1.3L9 6v2a1 1 0 0 1-1 1A8 8 0 0 1 1 2a1 1 0 0 1 1-1z"/></svg>
          (+618) 8123 4567 |
          <svg class="contact__icon" viewBox="0 0 10 10"><path d="M1 2h8v6H1z M1 2l4 3 4-3" fill="none" stroke="#1d4f86" stroke-width="1"/></svg>
          info@tvrb.com.au
        </div>
        <div>www.tvrb.com.au</div>
      </address>
    </header>

    <footer class="footer">
      <svg class="footer__swoop" viewBox="0 0 422 100" preserveAspectRatio="none">
        <defs>
          <linearGradient id="swoopGreyB" x1="0" x2="1">
            <stop offset="0" stop-color="#6d6e70"/>
            <stop offset="1" stop-color="#d6d7d9"/>
          </linearGradient>
          <linearGradient id="bandBlueB" x1="0" x2="1">
            <stop offset="0" stop-color="#2a8fc4"/>
            <stop offset="1" stop-color="#163f6e"/>
          </linearGradient>
        </defs>
        <path d="M0 58 C120 66 240 76 330 85 C230 81 110 73 0 66 Z" fill="url(#swoopGreyB)"/>
        <path d="M0 71 C130 86 300 92 422 70 V100 H0 Z" fill="url(#bandBlueB)"/>
      </svg>
      <div class="footer__brand">
        <span class="footer__name">TVRB</span>
        <span class="footer__square"></span>
      </div>
    </footer>
  </section>

</main>
</body>
</html>
```